Modern Design Business Card industrial maintenance company

Business card design for Company named Brookvale Equipment Services

Target Market(s)

Industrial

Industry/Entity Type

Maintenance and repair

Contact Information for Business Card

Place holder for address, office phone, mobile number and email

Requirements
Must have
• Clean modern look
Nice to have
• N/a

```html
<!DOCTYPE html>
<html lang="en">
<head>
<meta charset="utf-8">
<title>Brookvale Equipment Services – Business Card</title>
<link href="https://fonts.googleapis.com/css2?family=Barlow:wght@500;600;700&family=Barlow+Semi+Condensed:wght@600&display=swap" rel="stylesheet">
<style>
  :root {
    --ink: #111111;
    --paper: #ffffff;
    --frame: #9a9a9a;
    --icon: #7a7a7a;
    --label: #8a8a8a;
    --ghost-light: #efefef;
    --ghost-dark: rgba(255,255,255,0.08);
  }
  * { margin: 0; padding: 0; box-sizing: border-box; }
  html, body {
    width: 1200px; height: 1000px; overflow: hidden;
    background: var(--paper);
    font-family: "Barlow", Arial, sans-serif;
  }
  .card {
    position: absolute; left: 282px; width: 638px; height: 364px;
    overflow: hidden;
  }
  .card--front { top: 102px; background: var(--paper); border: 1px solid var(--frame); }
  .card--back {
    top: 555px;
    background: radial-gradient(circle at 160px 150px, #5b5e61 0%, #2c2d2f 30%, #0a0a0a 60%, #000 100%);
  }
  .ghost-ring { position: absolute; left: 20px; top: 36px; }
  .card--back .ghost-ring { top: 34px; }

  .brand { position: absolute; display: flex; align-items: center; }
  .brand__mark { flex: none; border-radius: 50%; }
  .brand__name {
    font-family: "Barlow Semi Condensed", "Barlow", sans-serif;
    font-weight: 600; text-transform: uppercase; line-height: 1;
  }
  .card--front .brand { left: 268px; top: 26px; gap: 16px; }
  .card--front .brand__mark { width: 78px; height: 78px; border: 4px solid var(--ink); }
  .card--front .brand__name { color: var(--ink); font-size: 27px; letter-spacing: 1px; }
  .card--front .brand__name small { display: block; font-size: 14.5px; letter-spacing: 3.4px; margin-top: 4px; }

  .card--back .brand { left: 0; right: 0; top: 106px; flex-direction: column; gap: 14px; }
  .card--back .brand__mark { width: 106px; height: 106px; border: 5px solid #fff; }
  .card--back .brand__name { color: #fff; font-size: 31px; letter-spacing: 1.4px; text-align: center; }
  .card--back .brand__name small { display: block; font-size: 14.5px; letter-spacing: 4.6px; margin-top: 5px; }

  .holder-name {
    position: absolute; left: 101px; top: 170px;
    font-size: 26px; font-weight: 600; color: var(--ink); letter-spacing: 0.3px;
  }
  .contact { position: absolute; left: 342px; top: 236px; list-style: none; }
  .contact li {
    display: flex; align-items: center; height: 26.5px;
    font-size: 15px; font-weight: 600; color: var(--ink);
  }
  .contact svg { width: 18px; height: 20px; margin-right: 7px; fill: var(--icon); flex: none; }

  .side-label {
    position: absolute; left: 0; width: 1200px; text-align: center;
    font-size: 16px; font-weight: 500; color: var(--label); letter-spacing: 0.3px;
  }
</style>
</head>
<body>

<section class="card card--front">
  <svg class="ghost-ring" width="292" height="292" viewBox="0 0 292 292" aria-hidden="true">
    <circle cx="146" cy="146" r="140" fill="none" stroke="var(--ghost-light)" stroke-width="7"/>
  </svg>

  <div class="brand">
    <span class="brand__mark"></span>
    <p class="brand__name">Brookvale<small>Equipment Services</small></p>
  </div>

  <p class="holder-name">NAME HERE</p>

  <ul class="contact">
    <li><svg viewBox="0 0 18 20"><path d="M9 1a6 6 0 0 0-6 6c0 4.5 6 12 6 12s6-7.5 6-12a6 6 0 0 0-6-6zm0 8.4A2.4 2.4 0 1 1 9 4.6a2.4 2.4 0 0 1 0 4.8z"/></svg>Address street, Region, City 12345</li>
    <li><svg viewBox="0 0 18 20"><path d="M5 0h8a2 2 0 0 1 2 2v16a2 2 0 0 1-2 2H5a2 2 0 0 1-2-2V2a2 2 0 0 1 2-2zm0 2v16h8V2z"/></svg>555-214-3086</li>
    <li><svg viewBox="0 0 18 20"><path d="M4 3l3 0 1.5 4-2 1.3a9 9 0 0 0 4.2 4.2L12 10.5l4 1.5v3c0 1-1 2-2 2C8 17 2 11 2 5c0-1 1-2 2-2z"/></svg>555-208-7741</li>
    <li><svg viewBox="0 0 18 20"><path d="M1 5h16v11H1zm1.5 1.3v.4L9 11l6.5-4.3v-.4zM2.5 8.3v6.4h13V8.3L9 12.6z"/></svg>email@brookvaleequipment.com</li>
  </ul>
</section>
<p class="side-label" style="top:482px">Front Side</p>

<section class="card card--back">
  <svg class="ghost-ring" width="292" height="292" viewBox="0 0 292 292" aria-hidden="true">
    <circle cx="146" cy="146" r="140" fill="none" stroke="var(--ghost-dark)" stroke-width="7"/>
  </svg>
  <div class="brand">
    <span class="brand__mark"></span>
    <p class="brand__name">Brookvale<small>Equipment Services</small></p>
  </div>
</section>
<p class="side-label" style="top:942px">Back Side</p>

</body>
</html>
```